Real Estate Sales and Marketing brochures

I have a few templates I uploaded of my old presentations and what I would like to see as a new presentation. I need 1 buyer (7-10 slides), 1 seller (8-12 slides), and 1 about me|us (4-5 slides) presentation. Those 3 would most likely contain 1-2 of the same slides and be 7-10 slides away. I would like it in power point presentation as well as pdf.

I am looking for something very clean, consistent, crisp, bright pictures (of the North Ga area.. Lake Morrow, North Ga Mtns, and the town of Forsyth County along with some really nice homes as the background). I have permission to use this photographers photos (he is my photographer). http://www.corvinstudio.net (go to interiors and exteriors) and http://blog.corvinstudio.net

The goal is to WoW people like my friends presentation labeled RMT does and 1: tell them what they will get with the list their home with us 2: when the buy with us and 3: who we are and what we have accomplished.

If I can get going in the right direction I would like to add stationary, letterhead, etc. to the order. My goal is to have great presentations and then have my flyers and all other printed materials match.

Target Market(s)

Buyers, sellers, and investors in the Real Estate Industry.

Industry/Entity Type

Real Estate Agent

Font styles to use
Serif

Colors
f04a50
85acd3

Requirements
Must have
• 1. about us 2. our services 3. our achievements 4. the process 5. about HB.
• Over 100m in sales (numbers and other awards can be seen at harborwithhale.net). Voted Best of Forsyth County by our Clients, 141,000 total votes, in the Ridgefield Ledger. North Ga's sole Realtor for Home Advisors We Rely On program.
Nice to have
• NICE clean pictures as the background
Should not have
• Dates on any logos or information other than achievements

```html
<!DOCTYPE html>
<html lang="en">
<head>
<meta charset="utf-8">
<title>Why Do You Need a Realtor</title>
<link rel="stylesheet" href="https://fonts.googleapis.com/css2?family=Carlito:ital,wght@0,400;0,700;1,700&display=swap">
<style>
  :root {
    --photo-light: #5d9cc4;
    --photo-deep: #1d3f63;
    --stone: #f3f3f2;
    --band: #383838;
    --panel: rgba(70, 70, 70, 0.74);
    --panel-edge: #1e1e1e;
    --ink: #ffffff;
  }
  html, body {
    margin: 0;
    padding: 0;
    overflow: hidden;
    background: #ffffff;
  }
  .slide {
    position: relative;
    width: 1200px;
    height: 675px;
    overflow: hidden;
    background: var(--stone);
    font-family: "Carlito", Calibri, sans-serif;
    color: var(--ink);
  }
  .lake-view {
    position: absolute;
    left: 0;
    top: 0;
    width: 888px;
    height: 675px;
    background: linear-gradient(180deg, var(--photo-light) 0%, var(--photo-deep) 100%);
  }
  .stone-strip {
    position: absolute;
    left: 888px;
    top: 0;
    width: 223px;
    height: 675px;
    background: var(--stone);
  }
  .edge-band {
    position: absolute;
    left: 1111px;
    top: 0;
    width: 89px;
    height: 675px;
    background: var(--band);
  }
  .info-panel {
    position: absolute;
    left: 267px;
    top: 75px;
    width: 933px;
    height: 520px;
    box-sizing: border-box;
    background: var(--panel);
    border: 1px solid var(--panel-edge);
    border-right: none;
    padding: 0 40px 0 9px;
  }
  .info-panel__title {
    margin: 12px 0 0;
    text-align: center;
    font-weight: 400;
    font-size: 39px;
    letter-spacing: -0.3px;
    line-height: 48px;
    padding-left: 16px;
  }
  .info-panel__intro {
    margin: 53px 0 0;
    font-size: 17px;
    line-height: 24px;
    letter-spacing: 0;
  }
  .guide-heading {
    margin: 49px 0 0;
    font-weight: 700;
    font-size: 12.5px;
    line-height: 16px;
    font-variant: small-caps;
    letter-spacing: 0.1px;
  }
  .benefits {
    list-style: none;
    margin: 20px 0 0;
    padding: 0;
    font-weight: 700;
    font-size: 13.8px;
    line-height: 19.7px;
    letter-spacing: -0.25px;
  }
  .benefits__item {
    position: relative;
    padding-left: 18px;
  }
  .benefits__tick {
    position: absolute;
    left: 0;
    top: 4px;
    width: 11px;
    height: 11px;
  }
</style>
</head>
<body>
  <main class="slide">
    <div class="lake-view" role="img" aria-label="Aerial photograph of a lake with wooded peninsulas under a clear sky"></div>
    <div class="stone-strip" role="img" aria-label="Soft white marble texture"></div>
    <div class="edge-band"></div>

    <section class="info-panel">
      <h1 class="info-panel__title">WHY DO YOU NEED A REALTOR</h1>

      <p class="info-panel__intro">As a licensed real estate professional I provide much more than the service of helping you find your ideal home. Realtors are expert negotiators with other agents, seasoned financial advisors with clients, and superb navigators around the local neighborhood. They are members of the National Guild of Home Advisors (NGHA) and must abide by a Code of Ethics and Standards of Practice enforced by the NGHA. A professional Realtor is your best resource when buying your home.</p>

      <p class="guide-heading">Let Me be Your Guide —</p>

      <ul class="benefits">
        <li class="benefits__item"><svg class="benefits__tick" viewBox="0 0 12 12"><path d="M1 6.5 L4.5 10 L11 1.5" fill="none" stroke="#ffffff" stroke-width="1.6"/></svg>I can save you endless amounts of time, money, and frustration.</li>
        <li class="benefits__item"><svg class="benefits__tick" viewBox="0 0 12 12"><path d="M1 6.5 L4.5 10 L11 1.5" fill="none" stroke="#ffffff" stroke-width="1.6"/></svg>I know the housing market inside and out and can help you avoid the “wild goose chase.”</li>
        <li class="benefits__item"><svg class="benefits__tick" viewBox="0 0 12 12"><path d="M1 6.5 L4.5 10 L11 1.5" fill="none" stroke="#ffffff" stroke-width="1.6"/></svg>I can help you with <em>any</em> home, even if it is listed elsewhere or if it is being sold directly by the owner.</li>
        <li class="benefits__item"><svg class="benefits__tick" viewBox="0 0 12 12"><path d="M1 6.5 L4.5 10 L11 1.5" fill="none" stroke="#ffffff" stroke-width="1.6"/></svg>I know the best lenders in the area and can help you understand the importance of being pre-qualified for a mortgage. I can also discuss down payments, closing costs, and monthly payment options that suit you.</li>
        <li class="benefits__item"><svg class="benefits__tick" viewBox="0 0 12 12"><path d="M1 6.5 L4.5 10 L11 1.5" fill="none" stroke="#ffffff" stroke-width="1.6"/></svg>I am an excellent source for both general and specific information about the community such as schools, churches, shopping, and transportation - - plus tips on home inspections and pricing.</li>
        <li class="benefits__item"><svg class="benefits__tick" viewBox="0 0 12 12"><path d="M1 6.5 L4.5 10 L11 1.5" fill="none" stroke="#ffffff" stroke-width="1.6"/></svg>I am experienced at presenting your offer to the homeowner and can help you through the process of negotiating the best price. We bring objectivity to the buying transaction, and we can point out the advantages and the disadvantages of a particular property.</li>
      </ul>
    </section>
  </main>
</body>
</html>
```